Fun A1 2012 family planner using clever typography and block colour

I have been looking for an A1 2012 family planner and I have not been able to find one. Hence I would like help to develop such a planner. I plan to print it on matt paper, portrait orientated. I have attached some reference pictures of our 2011 planner. I like interesting typography, clear clean colours and simple illustration. I need space to write in daily events and need the weeks and days to be clearly delineated from each other. Each day cell needs the date and day in it (please refer to the file uploaded for a visual reference confirming this). Each weekend needs some kind of colour/ typographic delineation. I want a design for a year-at-a-view calendar. I plan to print the planner in Sydney, Australia with brightmarkprinthouse.com.au and probably to sell printed copies online. The terms & conditions of this project are that I will own the design concept 100% and in perpetuity worldwide once payment has been made. (NB. The attached Work File in Word contains a rough layout and all months, days and dates all typed up to make for quicker design.)

Target Market(s)

Reasonably well heeled family of 4. 2 parents. 2 kids. 2 pets.

Industry/Entity Type

Events

Requirements
Must have
• The calendar must be portrait (not landscape orientated), A1 size. It will be printed on matt paper by brightmarkprinthouse.com.au. It must have months running left to right (Jan-Dec) and day/date cells running top to bottom (refer 2011 planner photos in file uploaded). The day/ date cells must be around 3(w)x2(h)cm - big enough to write daily events in. Weekends must be colour/ typographically delineated. 2012 year must be noted as must "A Paperkite Inc Project" and web address in fine print bottom left hand left hand corner.
Nice to have
• A Paperkite Inc logo in bottom left hand corder (perhaps Merry Otter like: http://www.pixelvault-example.com/design_submission.aspx?designid=731604). Header/Footer space for customisation (e.g. "Brandt-Osei 2012 Planner" or "QRN Co 2012 Planner".
Should not have
• The calendar should not use photographs or resemble standard or cheesy wall calendars. No watermarks please.

```html
<!DOCTYPE html>
<html lang="en">
<head>
<meta charset="utf-8">
<title>2012 Family Planner</title>
<link rel="stylesheet" href="https://fonts.googleapis.com/css2?family=Open+Sans:wght@300;400&family=Roboto+Condensed:wght@300;700&display=swap">
<style>
:root{
  --jan:#86d1c4;--feb:#fbb04c;--mar:#a37ab1;--apr:#afd68c;
  --may:#f47b2f;--jun:#e01a5f;--jul:#18a99a;--aug:#d5de24;
  --sep:#ef4237;--oct:#b19b47;--nov:#9a1c5f;--dec:#4a4a4c;
  --ink:#4a4a4c;--paper:#ffffff;
}
*{box-sizing:border-box;margin:0;padding:0}
html,body{width:848px;height:1200px;overflow:hidden;background:var(--paper)}
.planner{position:relative;width:848px;height:1200px}
.year-title{position:absolute;left:1px;top:-7px;font:300 38px/1 'Open Sans',sans-serif;color:var(--jan);z-index:2}
.months{position:absolute;left:6px;top:30px;display:grid;grid-template-columns:repeat(12,62px);column-gap:5.7px}
.month-name{height:33px;background:var(--c);color:#fff;font:400 15px/1 'Open Sans',sans-serif;padding:1px 0 0 2px}
.days{list-style:none;margin-top:5px}
.days li{position:relative;height:34.4px}
.days b{position:absolute;left:0;top:0;width:17px;height:25px;border:1.5px solid var(--c);writing-mode:vertical-rl;transform:rotate(180deg);font:300 15px/14px 'Roboto Condensed',sans-serif;color:var(--c);text-align:center}
.days li.w b{background:var(--c);color:#fff}
.days i{position:absolute;left:20px;top:2px;font:700 6.5px/1 'Roboto Condensed',sans-serif;font-style:normal;color:var(--c)}
.jan{--c:var(--jan)}.feb{--c:var(--feb)}.mar{--c:var(--mar)}.apr{--c:var(--apr)}
.may{--c:var(--may)}.jun{--c:var(--jun)}.jul{--c:var(--jul)}.aug{--c:var(--aug)}
.sep{--c:var(--sep)}.oct{--c:var(--oct)}.nov{--c:var(--nov)}.dec{--c:var(--dec)}
.brand{position:absolute;left:58px;top:1136px;font:700 8px/1 'Roboto Condensed',sans-serif;letter-spacing:1.5px;text-transform:uppercase;color:var(--ink);white-space:nowrap}
</style>
</head>
<body>
<main class="planner">
<h1 class="year-title">2012</h1>
<div class="months">

<section class="month jan"><h2 class="month-name">JAN</h2><ul class="days">
<li class="w"><b>01</b><i>SUNDAY</i></li><li><b>02</b><i>MONDAY</i></li><li><b>03</b><i>TUESDAY</i></li><li><b>04</b><i>WEDNESDAY</i></li><li><b>05</b><i>THURSDAY</i></li><li><b>06</b><i>FRIDAY</i></li><li class="w"><b>07</b><i>SATURDAY</i></li>
<li class="w"><b>08</b><i>SUNDAY</i></li><li><b>09</b><i>MONDAY</i></li><li><b>10</b><i>TUESDAY</i></li><li><b>11</b><i>WEDNESDAY</i></li><li><b>12</b><i>THURSDAY</i></li><li><b>13</b><i>FRIDAY</i></li><li class="w"><b>14</b><i>SATURDAY</i></li>
<li class="w"><b>15</b><i>SUNDAY</i></li><li><b>16</b><i>MONDAY</i></li><li><b>17</b><i>TUESDAY</i></li><li><b>18</b><i>WEDNESDAY</i></li><li><b>19</b><i>THURSDAY</i></li><li><b>20</b><i>FRIDAY</i></li><li class="w"><b>21</b><i>SATURDAY</i></li>
<li class="w"><b>22</b><i>SUNDAY</i></li><li><b>23</b><i>MONDAY</i></li><li><b>24</b><i>TUESDAY</i></li><li><b>25</b><i>WEDNESDAY</i></li><li><b>26</b><i>THURSDAY</i></li><li><b>27</b><i>FRIDAY</i></li><li class="w"><b>28</b><i>SATURDAY</i></li>
<li class="w"><b>29</b><i>SUNDAY</i></li><li><b>30</b><i>MONDAY</i></li><li><b>31</b><i>TUESDAY</i></li>
</ul></section>

<section class="month feb"><h2 class="month-name">FEB</h2><ul class="days">
<li><b>01</b><i>WEDNESDAY</i></li><li><b>02</b><i>THURSDAY</i></li><li><b>03</b><i>FRIDAY</i></li><li class="w"><b>04</b><i>SATURDAY</i></li><li class="w"><b>05</b><i>SUNDAY</i></li>
<li><b>06</b><i>MONDAY</i></li><li><b>07</b><i>TUESDAY</i></li><li><b>08</b><i>WEDNESDAY</i></li><li><b>09</b><i>THURSDAY</i></li><li><b>10</b><i>FRIDAY</i></li><li class="w"><b>11</b><i>SATURDAY</i></li><li class="w"><b>12</b><i>SUNDAY</i></li>
<li><b>13</b><i>MONDAY</i></li><li><b>14</b><i>TUESDAY</i></li><li><b>15</b><i>WEDNESDAY</i></li><li><b>16</b><i>THURSDAY</i></li><li><b>17</b><i>FRIDAY</i></li><li class="w"><b>18</b><i>SATURDAY</i></li><li class="w"><b>19</b><i>SUNDAY</i></li>
<li><b>20</b><i>MONDAY</i></li><li><b>21</b><i>TUESDAY</i></li><li><b>22</b><i>WEDNESDAY</i></li><li><b>23</b><i>THURSDAY</i></li><li><b>24</b><i>FRIDAY</i></li><li class="w"><b>25</b><i>SATURDAY</i></li><li class="w"><b>26</b><i>SUNDAY</i></li>
<li><b>27</b><i>MONDAY</i></li><li><b>28</b><i>TUESDAY</i></li><li><b>29</b><i>WEDNESDAY</i></li>
</ul></section>

<section class="month mar"><h2 class="month-name">MAR</h2><ul class="days">
<li><b>01</b><i>THURSDAY</i></li><li><b>02</b><i>FRIDAY</i></li><li class="w"><b>03</b><i>SATURDAY</i></li><li class="w"><b>04</b><i>SUNDAY</i></li>
<li><b>05</b><i>MONDAY</i></li><li><b>06</b><i>TUESDAY</i></li><li><b>07</b><i>WEDNESDAY</i></li><li><b>08</b><i>THURSDAY</i></li><li><b>09</b><i>FRIDAY</i></li><li class="w"><b>10</b><i>SATURDAY</i></li><li class="w"><b>11</b><i>SUNDAY</i></li>
<li><b>12</b><i>MONDAY</i></li><li><b>13</b><i>TUESDAY</i></li><li><b>14</b><i>WEDNESDAY</i></li><li><b>15</b><i>THURSDAY</i></li><li><b>16</b><i>FRIDAY</i></li><li class="w"><b>17</b><i>SATURDAY</i></li><li class="w"><b>18</b><i>SUNDAY</i></li>
<li><b>19</b><i>MONDAY</i></li><li><b>20</b><i>TUESDAY</i></li><li><b>21</b><i>WEDNESDAY</i></li><li><b>22</b><i>THURSDAY</i></li><li><b>23</b><i>FRIDAY</i></li><li class="w"><b>24</b><i>SATURDAY</i></li><li class="w"><b>25</b><i>SUNDAY</i></li>
<li><b>26</b><i>MONDAY</i></li><li><b>27</b><i>TUESDAY</i></li><li><b>28</b><i>WEDNESDAY</i></li><li><b>29</b><i>THURSDAY</i></li><li><b>30</b><i>FRIDAY</i></li><li class="w"><b>31</b><i>SATURDAY</i></li>
</ul></section>

<section class="month apr"><h2 class="month-name">APR</h2><ul class="days">
<li class="w"><b>01</b><i>SUNDAY</i></li><li><b>02</b><i>MONDAY</i></li><li><b>03</b><i>TUESDAY</i></li><li><b>04</b><i>WEDNESDAY</i></li><li><b>05</b><i>THURSDAY</i></li><li><b>06</b><i>FRIDAY</i></li><li class="w"><b>07</b><i>SATURDAY</i></li>
<li class="w"><b>08</b><i>SUNDAY</i></li><li><b>09</b><i>MONDAY</i></li><li><b>10</b><i>TUESDAY</i></li><li><b>11</b><i>WEDNESDAY</i></li><li><b>12</b><i>THURSDAY</i></li><li><b>13</b><i>FRIDAY</i></li><li class="w"><b>14</b><i>SATURDAY</i></li>
<li class="w"><b>15</b><i>SUNDAY</i></li><li><b>16</b><i>MONDAY</i></li><li><b>17</b><i>TUESDAY</i></li><li><b>18</b><i>WEDNESDAY</i></li><li><b>19</b><i>THURSDAY</i></li><li><b>20</b><i>FRIDAY</i></li><li class="w"><b>21</b><i>SATURDAY</i></li>
<li class="w"><b>22</b><i>SUNDAY</i></li><li><b>23</b><i>MONDAY</i></li><li><b>24</b><i>TUESDAY</i></li><li><b>25</b><i>WEDNESDAY</i></li><li><b>26</b><i>THURSDAY</i></li><li><b>27</b><i>FRIDAY</i></li><li class="w"><b>28</b><i>SATURDAY</i></li>
<li class="w"><b>29</b><i>SUNDAY</i></li><li><b>30</b><i>MONDAY</i></li>
</ul></section>

<section class="month may"><h2 class="month-name">MAY</h2><ul class="days">
<li><b>01</b><i>TUESDAY</i></li><li><b>02</b><i>WEDNESDAY</i></li><li><b>03</b><i>THURSDAY</i></li><li><b>04</b><i>FRIDAY</i></li><li class="w"><b>05</b><i>SATURDAY</i></li><li class="w"><b>06</b><i>SUNDAY</i></li>
<li><b>07</b><i>MONDAY</i></li><li><b>08</b><i>TUESDAY</i></li><li><b>09</b><i>WEDNESDAY</i></li><li><b>10</b><i>THURSDAY</i></li><li><b>11</b><i>FRIDAY</i></li><li class="w"><b>12</b><i>SATURDAY</i></li><li class="w"><b>13</b><i>SUNDAY</i></li>
<li><b>14</b><i>MONDAY</i></li><li><b>15</b><i>TUESDAY</i></li><li><b>16</b><i>WEDNESDAY</i></li><li><b>17</b><i>THURSDAY</i></li><li><b>18</b><i>FRIDAY</i></li><li class="w"><b>19</b><i>SATURDAY</i></li><li class="w"><b>20</b><i>SUNDAY</i></li>
<li><b>21</b><i>MONDAY</i></li><li><b>22</b><i>TUESDAY</i></li><li><b>23</b><i>WEDNESDAY</i></li><li><b>24</b><i>THURSDAY</i></li><li><b>25</b><i>FRIDAY</i></li><li class="w"><b>26</b><i>SATURDAY</i></li><li class="w"><b>27</b><i>SUNDAY</i></li>
<li><b>28</b><i>MONDAY</i></li><li><b>29</b><i>TUESDAY</i></li><li><b>30</b><i>WEDNESDAY</i></li><li><b>31</b><i>THURSDAY</i></li>
</ul></section>

<section class="month jun"><h2 class="month-name">JUN</h2><ul class="days">
<li><b>01</b><i>FRIDAY</i></li><li class="w"><b>02</b><i>SATURDAY</i></li><li class="w"><b>03</b><i>SUNDAY</i></li>
<li><b>04</b><i>MONDAY</i></li><li><b>05</b><i>TUESDAY</i></li><li><b>06</b><i>WEDNESDAY</i></li><li><b>07</b><i>THURSDAY</i></li><li><b>08</b><i>FRIDAY</i></li><li class="w"><b>09</b><i>SATURDAY</i></li><li class="w"><b>10</b><i>SUNDAY</i></li>
<li><b>11</b><i>MONDAY</i></li><li><b>12</b><i>TUESDAY</i></li><li><b>13</b><i>WEDNESDAY</i></li><li><b>14</b><i>THURSDAY</i></li><li><b>15</b><i>FRIDAY</i></li><li class="w"><b>16</b><i>SATURDAY</i></li><li class="w"><b>17</b><i>SUNDAY</i></li>
<li><b>18</b><i>MONDAY</i></li><li><b>19</b><i>TUESDAY</i></li><li><b>20</b><i>WEDNESDAY</i></li><li><b>21</b><i>THURSDAY</i></li><li><b>22</b><i>FRIDAY</i></li><li class="w"><b>23</b><i>SATURDAY</i></li><li class="w"><b>24</b><i>SUNDAY</i></li>
<li><b>25</b><i>MONDAY</i></li><li><b>26</b><i>TUESDAY</i></li><li><b>27</b><i>WEDNESDAY</i></li><li><b>28</b><i>THURSDAY</i></li><li><b>29</b><i>FRIDAY</i></li><li class="w"><b>30</b><i>SATURDAY</i></li>
</ul></section>

<section class="month jul"><h2 class="month-name">JUL</h2><ul class="days">
<li class="w"><b>01</b><i>SUNDAY</i></li><li><b>02</b><i>MONDAY</i></li><li><b>03</b><i>TUESDAY</i></li><li><b>04</b><i>WEDNESDAY</i></li><li><b>05</b><i>THURSDAY</i></li><li><b>06</b><i>FRIDAY</i></li><li class="w"><b>07</b><i>SATURDAY</i></li>
<li class="w"><b>08</b><i>SUNDAY</i></li><li><b>09</b><i>MONDAY</i></li><li><b>10</b><i>TUESDAY</i></li><li><b>11</b><i>WEDNESDAY</i></li><li><b>12</b><i>THURSDAY</i></li><li><b>13</b><i>FRIDAY</i></li><li class="w"><b>14</b><i>SATURDAY</i></li>
<li class="w"><b>15</b><i>SUNDAY</i></li><li><b>16</b><i>MONDAY</i></li><li><b>17</b><i>TUESDAY</i></li><li><b>18</b><i>WEDNESDAY</i></li><li><b>19</b><i>THURSDAY</i></li><li><b>20</b><i>FRIDAY</i></li><li class="w"><b>21</b><i>SATURDAY</i></li>
<li class="w"><b>22</b><i>SUNDAY</i></li><li><b>23</b><i>MONDAY</i></li><li><b>24</b><i>TUESDAY</i></li><li><b>25</b><i>WEDNESDAY</i></li><li><b>26</b><i>THURSDAY</i></li><li><b>27</b><i>FRIDAY</i></li><li class="w"><b>28</b><i>SATURDAY</i></li>
<li class="w"><b>29</b><i>SUNDAY</i></li><li><b>30</b><i>MONDAY</i></li><li><b>31</b><i>TUESDAY</i></li>
</ul></section>

<section class="month aug"><h2 class="month-name">AUG</h2><ul class="days">
<li><b>01</b><i>WEDNESDAY</i></li><li><b>02</b><i>THURSDAY</i></li><li><b>03</b><i>FRIDAY</i></li><li class="w"><b>04</b><i>SATURDAY</i></li><li class="w"><b>05</b><i>SUNDAY</i></li>
<li><b>06</b><i>MONDAY</i></li><li><b>07</b><i>TUESDAY</i></li><li><b>08</b><i>WEDNESDAY</i></li><li><b>09</b><i>THURSDAY</i></li><li><b>10</b><i>FRIDAY</i></li><li class="w"><b>11</b><i>SATURDAY</i></li><li class="w"><b>12</b><i>SUNDAY</i></li>
<li><b>13</b><i>MONDAY</i></li><li><b>14</b><i>TUESDAY</i></li><li><b>15</b><i>WEDNESDAY</i></li><li><b>16</b><i>THURSDAY</i></li><li><b>17</b><i>FRIDAY</i></li><li class="w"><b>18</b><i>SATURDAY</i></li><li class="w"><b>19</b><i>SUNDAY</i></li>
<li><b>20</b><i>MONDAY</i></li><li><b>21</b><i>TUESDAY</i></li><li><b>22</b><i>WEDNESDAY</i></li><li><b>23</b><i>THURSDAY</i></li><li><b>24</b><i>FRIDAY</i></li><li class="w"><b>25</b><i>SATURDAY</i></li><li class="w"><b>26</b><i>SUNDAY</i></li>
<li><b>27</b><i>MONDAY</i></li><li><b>28</b><i>TUESDAY</i></li><li><b>29</b><i>WEDNESDAY</i></li><li><b>30</b><i>THURSDAY</i></li><li><b>31</b><i>FRIDAY</i></li>
</ul></section>

<section class="month sep"><h2 class="month-name">SEP</h2><ul class="days">
<li class="w"><b>01</b><i>SATURDAY</i></li><li class="w"><b>02</b><i>SUNDAY</i></li>
<li><b>03</b><i>MONDAY</i></li><li><b>04</b><i>TUESDAY</i></li><li><b>05</b><i>WEDNESDAY</i></li><li><b>06</b><i>THURSDAY</i></li><li><b>07</b><i>FRIDAY</i></li><li class="w"><b>08</b><i>SATURDAY</i></li><li class="w"><b>09</b><i>SUNDAY</i></li>
<li><b>10</b><i>MONDAY</i></li><li><b>11</b><i>TUESDAY</i></li><li><b>12</b><i>WEDNESDAY</i></li><li><b>13</b><i>THURSDAY</i></li><li><b>14</b><i>FRIDAY</i></li><li class="w"><b>15</b><i>SATURDAY</i></li><li class="w"><b>16</b><i>SUNDAY</i></li>
<li><b>17</b><i>MONDAY</i></li><li><b>18</b><i>TUESDAY</i></li><li><b>19</b><i>WEDNESDAY</i></li><li><b>20</b><i>THURSDAY</i></li><li><b>21</b><i>FRIDAY</i></li><li class="w"><b>22</b><i>SATURDAY</i></li><li class="w"><b>23</b><i>SUNDAY</i></li>
<li><b>24</b><i>MONDAY</i></li><li><b>25</b><i>TUESDAY</i></li><li><b>26</b><i>WEDNESDAY</i></li><li><b>27</b><i>THURSDAY</i></li><li><b>28</b><i>FRIDAY</i></li><li class="w"><b>29</b><i>SATURDAY</i></li><li class="w"><b>30</b><i>SUNDAY</i></li>
</ul></section>

<section class="month oct"><h2 class="month-name">OCT</h2><ul class="days">
<li><b>01</b><i>MONDAY</i></li><li><b>02</b><i>TUESDAY</i></li><li><b>03</b><i>WEDNESDAY</i></li><li><b>04</b><i>THURSDAY</i></li><li><b>05</b><i>FRIDAY</i></li><li class="w"><b>06</b><i>SATURDAY</i></li><li class="w"><b>07</b><i>SUNDAY</i></li>
<li><b>08</b><i>MONDAY</i></li><li><b>09</b><i>TUESDAY</i></li><li><b>10</b><i>WEDNESDAY</i></li><li><b>11</b><i>THURSDAY</i></li><li><b>12</b><i>FRIDAY</i></li><li class="w"><b>13</b><i>SATURDAY</i></li><li class="w"><b>14</b><i>SUNDAY</i></li>
<li><b>15</b><i>MONDAY</i></li><li><b>16</b><i>TUESDAY</i></li><li><b>17</b><i>WEDNESDAY</i></li><li><b>18</b><i>THURSDAY</i></li><li><b>19</b><i>FRIDAY</i></li><li class="w"><b>20</b><i>SATURDAY</i></li><li class="w"><b>21</b><i>SUNDAY</i></li>
<li><b>22</b><i>MONDAY</i></li><li><b>23</b><i>TUESDAY</i></li><li><b>24</b><i>WEDNESDAY</i></li><li><b>25</b><i>THURSDAY</i></li><li><b>26</b><i>FRIDAY</i></li><li class="w"><b>27</b><i>SATURDAY</i></li><li class="w"><b>28</b><i>SUNDAY</i></li>
<li><b>29</b><i>MONDAY</i></li><li><b>30</b><i>TUESDAY</i></li><li><b>31</b><i>WEDNESDAY</i></li>
</ul></section>

<section class="month nov"><h2 class="month-name">NOV</h2><ul class="days">
<li><b>01</b><i>THURSDAY</i></li><li><b>02</b><i>FRIDAY</i></li><li class="w"><b>03</b><i>SATURDAY</i></li><li class="w"><b>04</b><i>SUNDAY</i></li>
<li><b>05</b><i>MONDAY</i></li><li><b>06</b><i>TUESDAY</i></li><li><b>07</b><i>WEDNESDAY</i></li><li><b>08</b><i>THURSDAY</i></li><li><b>09</b><i>FRIDAY</i></li><li class="w"><b>10</b><i>SATURDAY</i></li><li class="w"><b>11</b><i>SUNDAY</i></li>
<li><b>12</b><i>MONDAY</i></li><li><b>13</b><i>TUESDAY</i></li><li><b>14</b><i>WEDNESDAY</i></li><li><b>15</b><i>THURSDAY</i></li><li><b>16</b><i>FRIDAY</i></li><li class="w"><b>17</b><i>SATURDAY</i></li><li class="w"><b>18</b><i>SUNDAY</i></li>
<li><b>19</b><i>MONDAY</i></li><li><b>20</b><i>TUESDAY</i></li><li><b>21</b><i>WEDNESDAY</i></li><li><b>22</b><i>THURSDAY</i></li><li><b>23</b><i>FRIDAY</i></li><li class="w"><b>24</b><i>SATURDAY</i></li><li class="w"><b>25</b><i>SUNDAY</i></li>
<li><b>26</b><i>MONDAY</i></li><li><b>27</b><i>TUESDAY</i></li><li><b>28</b><i>WEDNESDAY</i></li><li><b>29</b><i>THURSDAY</i></li><li><b>30</b><i>FRIDAY</i></li>
</ul></section>

<section class="month dec"><h2 class="month-name">DEC</h2><ul class="days">
<li class="w"><b>01</b><i>SATURDAY</i></li><li class="w"><b>02</b><i>SUNDAY</i></li>
<li><b>03</b><i>MONDAY</i></li><li><b>04</b><i>TUESDAY</i></li><li><b>05</b><i>WEDNESDAY</i></li><li><b>06</b><i>THURSDAY</i></li><li><b>07</b><i>FRIDAY</i></li><li class="w"><b>08</b><i>SATURDAY</i></li><li class="w"><b>09</b><i>SUNDAY</i></li>
<li><b>10</b><i>MONDAY</i></li><li><b>11</b><i>TUESDAY</i></li><li><b>12</b><i>WEDNESDAY</i></li><li><b>13</b><i>THURSDAY</i></li><li><b>14</b><i>FRIDAY</i></li><li class="w"><b>15</b><i>SATURDAY</i></li><li class="w"><b>16</b><i>SUNDAY</i></li>
<li><b>17</b><i>MONDAY</i></li><li><b>18</b><i>TUESDAY</i></li><li><b>19</b><i>WEDNESDAY</i></li><li><b>20</b><i>THURSDAY</i></li><li><b>21</b><i>FRIDAY</i></li><li class="w"><b>22</b><i>SATURDAY</i></li><li class="w"><b>23</b><i>SUNDAY</i></li>
<li><b>24</b><i>MONDAY</i></li><li><b>25</b><i>TUESDAY</i></li><li><b>26</b><i>WEDNESDAY</i></li><li><b>27</b><i>THURSDAY</i></li><li><b>28</b><i>FRIDAY</i></li><li class="w"><b>29</b><i>SATURDAY</i></li><li class="w"><b>30</b><i>SUNDAY</i></li>
<li><b>31</b><i>MONDAY</i></li>
</ul></section>

</div>

<p class="brand">Merry Otter</p>
</main>
</body>
</html>
```